the letter head should have the logo ( may be top left), " Larkfield Health Institute" (may be top/middle ) and the two clinics info in a vertical column ( along the left side of the page )

other physicians and official letters

• the info provided in the attachements

```html
<!DOCTYPE html>
<html lang="en">
<head>
<meta charset="utf-8">
<title>Larkfield Health Institute – Stationery</title>
<link rel="stylesheet" href="https://fonts.googleapis.com/css2?family=Arimo:wght@400;700&family=Tinos:wght@400;700&display=swap">
<style>
  :root {
    --stage: #ececec;
    --stage-light: #f7f7f7;
    --paper: #ffffff;
    --paper-edge: rgba(0, 0, 0, 0.08);
    --shadow-soft: rgba(0, 0, 0, 0.16);
    --shadow-lift: rgba(0, 0, 0, 0.24);
    --brand-slate: #2f3a45;
    --brand-magenta: #a3286f;
    --ink: #2b2b2b;
    --body-grey: #9a9a9a;
    --heading-grey: #8a8a8a;
    --sign-tone: #d9d9d9;
  }
  * { box-sizing: border-box; margin: 0; padding: 0; }
  html, body { width: 1200px; height: 1200px; overflow: hidden; }
  body {
    background: radial-gradient(circle at 50% 45%, var(--stage-light) 0%, var(--stage) 70%);
    position: relative;
    font-family: "Tinos", "Times New Roman", serif;
  }

  .sheet { position: absolute; background: var(--paper); border: 1px solid var(--paper-edge); }
  .letterhead {
    left: 115px; top: 101px; width: 769px; height: 995px;
    box-shadow: 0 2px 8px var(--shadow-soft);
  }
  .envelope {
    left: 251px; top: 464px; width: 859px; height: 374px; z-index: 2;
    box-shadow: 0 3px 10px var(--shadow-lift), 0 0 2px var(--shadow-soft);
  }

  .brand { position: absolute; display: flex; align-items: center; gap: 8px; }
  .brand-square { width: 24px; height: 24px; background: var(--brand-slate); flex: none; }
  .brand-name { color: var(--brand-slate); font-family: "Tinos", serif; font-weight: 700; font-size: 16px; line-height: 17px; }
  .letterhead .brand { left: 609px; top: 18px; }
  .envelope .brand { left: 19px; top: 14px; }

  .offices { position: absolute; font-size: 10.5px; line-height: 14px; color: var(--ink); }
  .letterhead .offices { left: 613px; top: 104px; }
  .envelope .offices { left: 21px; top: 112px; }
  .office + .office { margin-top: 14px; }
  .office-name { color: var(--brand-magenta); font-weight: 700; font-size: 11px; margin-bottom: 2px; }
  .contact-line { display: flex; align-items: flex-start; gap: 5px; }
  .contact-line svg { width: 8px; height: 8px; margin-top: 3px; fill: var(--brand-magenta); flex: none; }
  .letterhead .contact-line { line-height: 14.5px; }
  .envelope .contact-line { line-height: 15.5px; }

  .letter-body { font-family: "Arimo", Arial, sans-serif; position: absolute; }
  .subject { left: 308px; top: 305px; font-size: 15px; color: var(--body-grey); letter-spacing: 0.2px; }
  .salutation { left: 42px; top: 337px; font-size: 16px; color: var(--heading-grey); }
  .copy { left: 42px; top: 370px; width: 440px; font-size: 11.5px; line-height: 12.8px; color: var(--body-grey); text-align: justify; }
  .copy p + p { margin-top: 25px; }
  .closing { left: 42px; top: 718px; font-size: 16px; color: var(--heading-grey); }
  .signer { left: 42px; top: 739px; font-size: 10px; font-weight: 700; color: var(--heading-grey); }
  .signature { position: absolute; left: 42px; top: 780px; width: 86px; height: 60px; background: var(--sign-tone); border-radius: 4px; }
</style>
</head>
<body>
<svg width="0" height="0" style="position:absolute" aria-hidden="true">
  <symbol id="icon-phone" viewBox="0 0 10 10"><path d="M2 0.5 L3.6 0.5 L4.2 2.8 L3 3.6 Q4 5.9 6.4 7 L7.2 5.8 L9.5 6.4 L9.5 8 Q9.5 9.5 8 9.5 Q0.5 8.5 0.5 2 Q0.5 0.5 2 0.5 Z"/></symbol>
  <symbol id="icon-fax" viewBox="0 0 10 10"><rect x="2.5" y="0.5" width="5" height="3"/><rect x="0.5" y="3.5" width="9" height="4" rx="1"/><rect x="2.5" y="6.5" width="5" height="3" fill="#fff" stroke="currentColor"/></symbol>
  <symbol id="icon-pin" viewBox="0 0 10 10"><path d="M5 0.3 Q8.6 0.3 8.6 3.8 Q8.6 6.2 5 9.7 Q1.4 6.2 1.4 3.8 Q1.4 0.3 5 0.3 Z M5 2.3 A1.5 1.5 0 1 0 5 5.3 A1.5 1.5 0 1 0 5 2.3 Z" fill-rule="evenodd"/></symbol>
</svg>

<section class="sheet letterhead">
  <div class="brand">
    <span class="brand-square"></span>
    <span class="brand-name">Larkfield<br>Health<br>Institute</span>
  </div>
  <div class="offices">
    <div class="office">
      <div class="office-name">Northgate Office</div>
      <div class="contact-line"><svg><use href="#icon-phone"/></svg>555-310-4420</div>
      <div class="contact-line"><svg><use href="#icon-fax"/></svg>555-310-4421</div>
      <div class="contact-line"><svg><use href="#icon-pin"/></svg><span>2180 W. Alder St.<br>Northgate 70412</span></div>
    </div>
    <div class="office">
      <div class="office-name">Riverside Office</div>
      <div class="contact-line"><svg><use href="#icon-phone"/></svg>555-728-6390</div>
      <div class="contact-line"><svg><use href="#icon-fax"/></svg>555-728-6391</div>
      <div class="contact-line"><svg><use href="#icon-pin"/></svg><span>740 E. College Ave.<br>Suite 212,70588</span></div>
    </div>
  </div>

  <div class="letter-body subject">SUB: ...........................................................</div>
  <div class="letter-body salutation">Dear Sir</div>
  <div class="letter-body copy">
    <p>Placeholder text stands in this space to show how a typical letter will read once it is printed on the page. It gives a fair sense of line length, spacing and tone for anyone reviewing the layout, so the final wording can be placed later without changing the overall balance of the sheet.</p>
    <p>It is a long standing habit to fill a draft with neutral wording while the real message is still being written. Readers then judge the spacing, margins and rhythm of the page rather than the meaning of each sentence, which keeps attention on the form.</p>
    <p>The point of using sample copy is that it has a natural spread of short and long words, so the block looks like ordinary prose. Many layouts use such wording as a starting point, and a search for sample copy will show many early versions. Over time new versions have appeared, some by accident and some on purpose, and they remain useful for reviewing a page before the final letter is ready.</p>
  </div>
  <div class="letter-body closing">Warm regards</div>
  <div class="letter-body signer">Nadia Verhoef M.D.</div>
  <div class="signature" role="img" aria-label="Handwritten signature of the physician"></div>
</section>

<section class="sheet envelope">
  <div class="brand">
    <span class="brand-square"></span>
    <span class="brand-name">Larkfield<br>Health<br>Institute</span>
  </div>
  <div class="offices">
    <div class="office">
      <div class="office-name">Northgate Office</div>
      <div class="contact-line"><svg><use href="#icon-phone"/></svg>555-310-4420</div>
      <div class="contact-line"><svg><use href="#icon-fax"/></svg>555-310-4421</div>
      <div class="contact-line"><svg><use href="#icon-pin"/></svg>2180 W. Alder St. Northgate 70412</div>
    </div>
    <div class="office">
      <div class="office-name">Riverside Office</div>
      <div class="contact-line"><svg><use href="#icon-phone"/></svg>555-728-6390</div>
      <div class="contact-line"><svg><use href="#icon-fax"/></svg>555-728-6391</div>
      <div class="contact-line"><svg><use href="#icon-pin"/></svg>740 E. College Ave. Suite 212,70588</div>
    </div>
  </div>
</section>
</body>
</html>
```